Yoga Studio Postcard Advertising Flyer

Need a postcard size flyer that will promote our business. The objective is to promote location and availability. Want it to be personal. The objective to connect the audience to the purpose of yoga and the focus on enabling functional well-being. Something that is a very big focus at this point in time in the world. I really want people to see the value in connecting with us via our website, classora app, linkhive or pixly. The colours are to be bright but not overwhelming and aligned to the logo colours. Its also important to have the location picture on the flyer - unless you think that it is way too much (try a with or without). I don't want this to be a specials brochure - it is an introduction to our brand and our business. No need to over do it with promotional lines apart from come and join us.
Updates

Delayed in organising this.

Target Market(s)

Local yogis and residence who are or want to be focused on well-being.

Requirements
Must have
• Pictures - would have the logo on one side.
Nice to have
• Modern and aligned to website design.

```html
<!DOCTYPE html>
<html lang="en">
<head>
<meta charset="utf-8">
<title>Amber Reed Yoga – Postcard Flyer</title>
<link rel="stylesheet" href="https://fonts.googleapis.com/css2?family=Outfit:wght@300;400;700;800&display=swap">
<style>
  :root {
    --sky: #2fa3dc;
    --navy: #1c1f3b;
    --white: #ffffff;
    --backdrop: #d4eaf6;
    --venue-sky: #9fb6cc;
    --venue-stone: #c4c6c8;
    --studio-wall: #e6ddd2;
    --studio-floor: #9a5f36;
    --portrait: #a9a9a9;
  }
  * { margin: 0; padding: 0; box-sizing: border-box; }
  html, body {
    width: 1200px; height: 842px; overflow: hidden;
    background: var(--backdrop);
    font-family: "Outfit", sans-serif;
  }
  .flyer {
    position: absolute; left: 316px; top: 21px;
    width: 568px; height: 800px;
    background: var(--white);
  }
  .contact-band {
    position: absolute; left: 0; top: 0; width: 568px; height: 292px;
    background: var(--sky); color: var(--white); text-align: center;
  }
  .brand-block {
    position: absolute; left: 209px; top: 0; width: 149px; height: 149px;
    background: var(--navy);
    display: flex; align-items: flex-end; justify-content: center;
    padding-bottom: 28px;
    font-weight: 400; font-size: 17px; line-height: 1.25; letter-spacing: 1.5px;
    color: var(--white); text-transform: uppercase;
  }
  .web-address {
    position: absolute; left: 0; top: 153px; width: 100%;
    font-weight: 800; font-size: 32px; line-height: 40px;
  }
  .channels-note {
    position: absolute; left: 0; top: 194px; width: 100%;
    font-weight: 400; font-size: 20px; line-height: 26px;
  }
  .channel-row {
    position: absolute; left: 0; top: 240px; width: 100%;
    display: flex; justify-content: center; gap: 22px;
  }
  .channel {
    display: flex; align-items: center; gap: 8px;
    font-weight: 700; font-size: 17px; line-height: 34px; color: var(--white);
  }
  .channel-mark {
    width: 34px; height: 34px; border-radius: 5px; background: var(--white);
  }
  .photo { position: absolute; top: 296px; height: 279px; }
  .photo-venue {
    left: 0; width: 280px;
    background: linear-gradient(180deg, var(--venue-sky) 0%, var(--venue-stone) 100%);
  }
  .photo-studio {
    left: 285px; width: 283px;
    background: linear-gradient(180deg, var(--studio-wall) 0%, var(--studio-wall) 40%, var(--studio-floor) 100%);
  }
  .portrait {
    position: absolute; left: 216px; top: 368px; width: 136px; height: 136px;
    border-radius: 50%; border: 4px solid var(--white);
    background: var(--portrait);
  }
  .info-band {
    position: absolute; left: 0; top: 579px; width: 568px; height: 221px;
    background: var(--navy); color: var(--white); text-align: center;
  }
  .address { position: absolute; left: 0; top: 27px; width: 100%; font-weight: 700; font-size: 19px; line-height: 26px; }
  .tagline { position: absolute; left: 0; top: 63px; width: 100%; font-weight: 300; font-size: 18px; line-height: 24px; }
  .vision { position: absolute; left: 60px; top: 97px; width: 448px; font-weight: 300; font-size: 18px; line-height: 25px; }
  .invite { position: absolute; left: 0; top: 156px; width: 100%; font-weight: 700; font-size: 34px; line-height: 42px; color: var(--sky); }
</style>
</head>
<body>
  <article class="flyer">
    <header class="contact-band">
      <div class="brand-block">Amber Reed<br>Yoga</div>
      <p class="web-address">www.amberreedyoga.com.au</p>
      <p class="channels-note">or find us on the classora App, linkhive or pixly</p>
      <div class="channel-row">
        <span class="channel"><span class="channel-mark"></span>classora</span>
        <span class="channel"><span class="channel-mark"></span>linkhive</span>
        <span class="channel"><span class="channel-mark"></span>pixly</span>
      </div>
    </header>
    <div class="photo photo-venue" role="img" aria-label="Photo of the historic stone chapel building that houses the studio"></div>
    <div class="photo photo-studio" role="img" aria-label="Photo of the sunlit studio interior with yoga mats on a timber floor"></div>
    <div class="portrait" role="img" aria-label="Black and white portrait of the yoga teacher"></div>
    <section class="info-band">
      <p class="address">The Chapel, 214 Harbour Lane Eastwood NSW 2122</p>
      <p class="tagline">Strengthen your well-being through adaptive yoga.</p>
      <p class="vision">Our vision is to create an atmosphere that enables inclusiveness of the whole community.</p>
      <p class="invite">Come join us!</p>
    </section>
  </article>
</body>
</html>
```